Business Card Design Project

I need a 2 sided business card - 1 side to promote my business "Brightfold Super" - and the other side to promote my fundraising initiative "OnTheSnapReel".

Please find attached photo referred to in my feedback email

Target Market(s)

Brightfold Super - financial professionals; OnTheSnapReel - anyone

Industry/Entity Type

Business

Requirements
Must have
• Must complement existing design work.

1. For Brightfold Super: Include orange block (with text Brightfold Super)
refer to www.brightfoldsuper.com.au and/or
https://www.facebook.com/BrightfoldSuper or other social media

2. must include in no particular order - Name: Maree Pellwood; Title: Managing Director; Website: www.brightfoldsuper.com.au; Email: maree@brightfoldsuper.com.au; Ph: 1300 462 915; website: http://aboutpage.example/mareepellwood; social media icons as per website ie FB, twitter, Google+, LinkedIn, YouTube, Pinterest

For OnTheSnapReel: https://www.facebook.com/OnTheSnapReel or other social media

1. must include in no particular order - Name: Maree Pellwood; Title: Founder; email: maree@brightfoldsuper.com.au; website: http://aboutpage.example/mareepellwood; social media icons as per website ie FB, twitter, Google+, LinkedIn, Pinterest
Nice to have
• For Brightfold Super: include dark block with tagline (eLearning, Competency, Performance) - either vertically or horizontally to orange block

For OnTheSnapReel: include tagline - Simply Fundraising

```html
<!DOCTYPE html>
<html lang="en">
<head>
<meta charset="utf-8">
<title>OnTheSnapReel – Business Card</title>
<link rel="stylesheet" href="https://fonts.googleapis.com/css2?family=Gentium+Book+Plus:wght@400;700&display=swap">
<style>
  :root {
    --lime: #b3c83f;
    --lime-deep: #a4bb2f;
    --lime-pale: #e9f0c4;
    --paper: #ffffff;
    --olive: #5b6b17;
    --ink: #111111;
    --flourish: #96ad2a;
    --icon: #6f8420;
  }
  html, body {
    margin: 0;
    padding: 0;
    width: 1200px;
    height: 844px;
    overflow: hidden;
    background: var(--paper);
  }
  .card {
    position: relative;
    width: 1200px;
    height: 844px;
    border-top-left-radius: 190px;
    overflow: hidden;
    background:
      radial-gradient(ellipse 520px 560px at 1210px 470px, var(--paper) 0%, var(--lime-pale) 40%, rgba(233,240,196,0) 100%),
      linear-gradient(100deg, var(--lime-deep) 0%, var(--lime) 55%, #c7d86a 100%);
    font-family: "Gentium Book Plus", "Palatino Linotype", serif;
  }
  .decor {
    position: absolute;
    border-radius: 50%;
  }
  .decor--butterfly {
    left: 560px; top: 150px; width: 330px; height: 300px;
    background: radial-gradient(ellipse at center, rgba(90,110,20,0.28) 0%, rgba(90,110,20,0) 70%);
  }
  .decor--vines-right {
    right: -60px; top: 0; width: 300px; height: 844px;
    background: radial-gradient(ellipse at 70% 50%, rgba(150,173,42,0.35) 0%, rgba(150,173,42,0) 70%);
  }
  .decor--vines-bottom {
    left: -40px; bottom: -80px; width: 620px; height: 260px;
    background: radial-gradient(ellipse at center, rgba(150,173,42,0.45) 0%, rgba(150,173,42,0) 70%);
  }
  .brand {
    position: absolute;
    left: 60px;
    top: 70px;
    width: 440px;
    text-align: center;
  }
  .brand__mark {
    display: block;
    width: 250px;
    height: 250px;
    margin: 0 auto 40px;
    border-radius: 50%;
    background: var(--paper);
  }
  .brand__name {
    margin: 0;
    color: var(--paper);
    font-weight: 700;
    font-size: 62px;
    line-height: 1;
  }
  .contact {
    position: absolute;
    left: 440px;
    top: 68px;
    width: 740px;
    text-align: center;
    margin: 0;
  }
  .contact__label {
    color: var(--olive);
    font-size: 38px;
    line-height: 1;
    margin: 0;
  }
  .contact__value {
    color: var(--ink);
    line-height: 1;
    margin: 0;
  }
  .contact__name { font-size: 54px; margin: 12px 0 20px; }
  .contact__email { font-size: 50px; margin: 14px 0 14px; }
  .contact__phone { margin: 0 0 20px; }
  .contact__phone .contact__value { font-size: 50px; }
  .contact__site { font-size: 50px; margin: 14px 0 20px; }
  .contact__about { font-size: 38px; margin: 18px 0 0; }
  .social {
    position: absolute;
    left: 588px;
    top: 712px;
    display: flex;
    gap: 32px;
    margin: 0;
    padding: 0;
    list-style: none;
  }
  .social__item {
    width: 72px;
    height: 72px;
    border-radius: 10px;
    background: var(--icon);
  }
</style>
</head>
<body>
  <main class="card">
    <div class="decor decor--vines-bottom" role="img" aria-label="Decorative floral vines"></div>
    <div class="decor decor--vines-right" role="img" aria-label="Decorative floral swirls"></div>
    <div class="decor decor--butterfly" role="img" aria-label="Faint butterfly decoration"></div>

    <div class="brand">
      <span class="brand__mark"></span>
      <h1 class="brand__name">OnTheSnapReel</h1>
    </div>

    <div class="contact">
      <p class="contact__label">Managing Director:</p>
      <p class="contact__value contact__name">Maree Pellwood</p>
      <p class="contact__label">Email:</p>
      <p class="contact__value contact__email">maree@brightfoldsuper.com.au</p>
      <p class="contact__phone"><span class="contact__label">Ph: </span><span class="contact__value">1300 462 915</span></p>
      <p class="contact__label">Website:</p>
      <p class="contact__value contact__site">www.brightfoldsuper.com.au</p>
      <p class="contact__label">Website:</p>
      <p class="contact__value contact__about">http://aboutpage.example/mareepellwood</p>
    </div>

    <ul class="social" aria-label="Social media links">
      <li class="social__item" role="img" aria-label="Social network link"></li>
      <li class="social__item" role="img" aria-label="Social network link"></li>
      <li class="social__item" role="img" aria-label="Social network link"></li>
      <li class="social__item" role="img" aria-label="Social network link"></li>
      <li class="social__item" role="img" aria-label="Social network link"></li>
      <li class="social__item" role="img" aria-label="Video channel link"></li>
    </ul>
  </main>
</body>
</html>
```